High end boutique food product label

We are looking for a label design to be used on our range of high end food products. We don't have a design or colour scheme in mind and are interested to see what ideas are submitted.
We would like it to feel sophisticated, chic, and eye-catching.
All of our products are handmade in Australia using Australian ingredients.
The graphics for the label will need to be scaleable to be fit a variety of labels from small squat jars with labels sized 3.5cm high and 7cm wide, to tall thin bottles with labels that are 14cm high and 4.5cm wide.
We would be interested in working with the winning designer to create these different sized labels.
The label submitted for this project should be 14cm high and 4.5cm wide, it should include our logo (file supplied in .jpeg and .ai), the product name 'Extra Virgin Olive Oil' and the size '250ml'.
This is just the front label on a bottle, we are not expecting a rear label to be created currently.
You are welcome to use any fonts you think will look good but the fonts used in our logo are Allaina Medium and Bebas Kai Regular.

```html
<!DOCTYPE html>
<html lang="en">
<head>
<meta charset="utf-8">
<title>Extra Virgin Olive Oil – Front Label Variations</title>
<link rel="stylesheet" href="https://fonts.googleapis.com/css2?family=Montserrat:wght@600;700&display=swap">
<style>
  :root {
    --canvas: #ffffff;
    --oil-brown: #432a1a;
    --frame-black: #000000;
    --frame-tan: #c0a882;
    --gold: #c9b088;
    --gold-soft: #b89d70;
  }
  * { margin: 0; padding: 0; box-sizing: border-box; }
  html, body {
    width: 1200px;
    height: 927px;
    overflow: hidden;
    background: var(--canvas);
  }
  .canvas {
    position: relative;
    width: 1200px;
    height: 927px;
    display: flex;
    justify-content: center;
    align-items: center;
    gap: 55px;
  }
  .label {
    width: 245px;
    height: 762px;
    display: block;
  }
  .label text {
    font-family: 'Montserrat', sans-serif;
    fill: var(--gold);
    text-anchor: middle;
  }
  .label .product-name { font-size: 29px; font-weight: 700; letter-spacing: 0.5px; }
  .label .origin { font-size: 11px; font-weight: 700; letter-spacing: 2.6px; }
  .label .volume { font-size: 22px; font-weight: 600; letter-spacing: 0.5px; }
  .label .brand-name { font-size: 17px; font-weight: 700; letter-spacing: 0.3px; }
  .label--black .frame { fill: var(--frame-black); }
  .label--tan .frame { fill: var(--frame-tan); }
  .label .drop { fill: var(--oil-brown); }
</style>
</head>
<body>
<main class="canvas">

  <svg class="label label--black" viewBox="0 0 350 1088" aria-label="Extra virgin olive oil label, black edges">
    <rect class="frame" width="350" height="1088"/>
    <path class="drop" d="M38,0 H311 V650 C311,720 280,760 230,785 C195,802 190,825 190,845 C190,870 205,880 225,895 A80,80 0 1 1 125,895 C145,880 158,870 158,845 C158,825 153,802 118,785 C68,760 38,720 38,650 Z"/>
    <rect x="88" y="102" width="175" height="196" rx="40" fill="url(#branchToneA)" role="img" aria-label="Hand-drawn olive branch with leaves and olives in gold line"/>
    <text class="product-name" x="175" y="470">EXTRA VIRGIN</text>
    <text class="product-name" x="175" y="503">OLIVE OIL</text>
    <text class="origin" x="175" y="543">100% AUSTRALIAN MADE</text>
    <text class="volume" x="175" y="707">250ML</text>
    <text class="brand-name" x="175" y="955">Wren &amp; Vale</text>
    <text class="brand-name" x="175" y="976">Pantry</text>
    <defs>
      <radialGradient id="branchToneA">
        <stop offset="0" stop-color="#8a7352"/>
        <stop offset="1" stop-color="#432a1a"/>
      </radialGradient>
    </defs>
  </svg>

  <svg class="label label--tan" viewBox="0 0 350 1088" aria-label="Extra virgin olive oil label, tan edges">
    <rect class="frame" width="350" height="1088"/>
    <path class="drop" d="M38,0 H311 V650 C311,720 280,760 230,785 C195,802 190,825 190,845 C190,870 205,880 225,895 A80,80 0 1 1 125,895 C145,880 158,870 158,845 C158,825 153,802 118,785 C68,760 38,720 38,650 Z"/>
    <rect x="88" y="102" width="175" height="196" rx="40" fill="url(#branchToneB)" role="img" aria-label="Hand-drawn olive branch with leaves and olives in gold line"/>
    <text class="product-name" x="175" y="470">EXTRA VIRGIN</text>
    <text class="product-name" x="175" y="503">OLIVE OIL</text>
    <text class="origin" x="175" y="543">100% AUSTRALIAN MADE</text>
    <text class="volume" x="175" y="707">250ML</text>
    <text class="brand-name" x="175" y="955">Wren &amp; Vale</text>
    <text class="brand-name" x="175" y="976">Pantry</text>
    <defs>
      <radialGradient id="branchToneB">
        <stop offset="0" stop-color="#8a7352"/>
        <stop offset="1" stop-color="#432a1a"/>
      </radialGradient>
    </defs>
  </svg>

</main>
</body>
</html>
```